Modern and Clean Web Re-Design Project

We have 2 companies in similar industries: Printing and Mail Preparation/Fulfillment. We prefer sites that are clean and easy to navigate.Our printing company, Harbourline Press Works' website, hpwdirect.example is outdated needs revamping. We have rebranded our logo and are looking for a new design that is clean, modern and geared to other corporations and business in the downtown Toronto area. Our mailing company, The Postwick Depot (thepostwickdepot.example) needs a website as well. This company is in the Direct Mail and letter shop business, which essentially is addressing/personalizing people's printed matter and preparing it for either the Canadian or US postal service. The Postwick Depot specializes in not-for-profit and corporate sectors.Please see our logos to get an idea of the colors and look we want. For all intensive purposes, the sites can look similar in design all we want is that each site has the appropriate corporate colors and is a bit different so they don't look identical as the two business run as separate corporations.The content of the website should be easily changed by our staff and we want it to be setup to optimized for SEO based on the keywords we want. We are looking for someone to work on this project immediately
Updates

Project Deadline Extended
Reason: Change of ideas

After doing some thinking, I would like the site to be more modern but the non flash sites that I have seen so far Im finding life-less and while I want something clean, not overly busy and corporate looking, I dont want the design to be bland looking.

Please design with the previous specs in mind but with a twist as mentioned above.

Thanks
Dorian

Target Market(s)

See above

Industry/Entity Type

Printing

Requirements
Must have
• Must match the design and style of each respective logoSee the attached impage of the front of our offices to have an idea of our lookWe must be able to edit the content ourselves without any fancy programs or tools.Must be SEO optimized
Nice to have
• An online order form that can be emailed to us for quotes.....perhaps a page with a bunch of fields that have drop down menus....
Should not have
• Should not be overly busy. I want it to be clean and simple but informative without being hard to navigate

```html
<!DOCTYPE html>
<html lang="en">
<head>
<meta charset="utf-8">
<title>Harbourline Press Works</title>
<link href="https://fonts.googleapis.com/css2?family=Arimo:wght@400;700&family=Didact+Gothic&display=swap" rel="stylesheet">
<style>
:root{
  --accent:#e8401c;
  --nav-active:#f7931e;
  --brown:#a0732e;
  --text:#666;
  --nav-bg:rgba(40,40,42,.88);
  --footer:#3a3a3a;
  --side:#8e9296;
  --frame:#eaeaea;
}
*{margin:0;padding:0;box-sizing:border-box}
html,body{width:1062px;height:1200px;overflow:hidden}
body{position:relative;background:#fff;font-family:"Arimo",Arial,sans-serif;color:var(--text)}
.hero{position:absolute;left:0;top:0;width:1062px;height:636px;
  background:
    radial-gradient(ellipse 70px 60px at 548px 218px,rgba(235,240,255,.95),rgba(160,180,230,.35) 45%,rgba(0,0,0,0) 100%),
    radial-gradient(ellipse 330px 140px at 640px 400px,rgba(176,88,52,.85),rgba(150,80,60,.35) 60%,rgba(0,0,0,0) 100%),
    radial-gradient(ellipse 80px 200px at 225px 320px,rgba(170,85,45,.7),rgba(0,0,0,0) 100%),
    radial-gradient(ellipse 620px 130px at 480px 600px,rgba(232,170,180,.9),rgba(0,0,0,0) 100%),
    linear-gradient(90deg,#454650 0%,#5a5760 40%,#4e4f5a 70%,#555560 100%)}
.hero-shade{position:absolute;left:0;top:0;width:1062px;height:636px;
  background:linear-gradient(180deg,rgba(30,30,38,.45) 0%,rgba(0,0,0,0) 30%,rgba(0,0,0,0) 75%,rgba(210,150,160,.35) 100%)}
.logo-box{position:absolute;left:79px;top:6px;width:265px;height:140px;background:#fff;
  display:flex;align-items:center;justify-content:center;gap:8px;box-shadow:0 1px 4px rgba(0,0,0,.3)}
.logo-box .dot{width:14px;height:14px;border-radius:50%;background:var(--accent)}
.logo-box .name{font-family:"Didact Gothic",sans-serif;font-size:17px;color:#8a6a4a;letter-spacing:.5px}
.top-contact{position:absolute;right:81px;top:22px;color:#fff;font-weight:700;font-size:14.5px}
.top-contact span{margin:0 12px}
.main-nav{position:absolute;left:417px;top:65px;width:566px;height:58px;background:var(--nav-bg);display:flex}
.main-nav a{color:#fff;text-decoration:none;font-size:13px;height:58px;line-height:58px;padding:0 18px}
.main-nav a.active{background:#000;color:var(--nav-active);border-top:3px solid var(--accent);line-height:52px;width:77px;text-align:center;padding:0}
.hero-arrow{position:absolute;top:299px;width:37px;height:37px}
.content{position:absolute;left:81px;top:662px;width:651px}
.content h1{font-family:"Didact Gothic",sans-serif;font-weight:400;font-size:22px;color:var(--accent);margin-bottom:9px}
.content p{font-size:12px;line-height:20.3px;text-align:justify;margin-bottom:7px}
.services{position:absolute;left:752px;top:667px;width:231px;list-style:none;border:1px solid #999}
.services li{height:37px;background:linear-gradient(#a5a9ad,var(--side));border-top:1px solid #c8cbce;
  display:flex;align-items:center;padding-left:14px;color:#fff;font-family:"Didact Gothic",sans-serif;font-size:17px;
  text-shadow:0 0 1px rgba(255,255,255,.8)}
.services li:first-child{background:linear-gradient(#7a7a7a,#444);border-top:0}
.services li svg{margin-right:12px;flex:none}
.divider{position:absolute;left:79px;top:915px;width:904px;border-top:1px solid #e3e3e3}
.works-title{position:absolute;left:0;width:1042px;top:929px;text-align:center;font-family:"Didact Gothic",sans-serif;font-weight:400;font-size:18px;color:var(--brown)}
.work{position:absolute;top:966px;width:195px;text-align:center}
.work .frame{height:119px;background:var(--frame);padding:5px}
.work .shot{width:100%;height:100%}
.work p{margin-top:12px;font-size:13.5px;color:var(--brown)}
.works-arrow{position:absolute;top:1016px}
.footer{position:absolute;left:0;top:1132px;width:1062px;height:68px;background:var(--footer);color:#ccc;font-size:11.5px}
.footer nav{position:absolute;left:79px;top:14px}
.footer nav a{color:#ccc;text-decoration:none}
.footer nav span{margin:0 8px}
.footer .copy{position:absolute;left:79px;top:40px}
.social{position:absolute;top:23px;width:22px;height:22px;border-radius:50%;background:#777}
</style>
</head>
<body>
<div class="hero" role="img" aria-label="Photo of the office reception area under construction, wood counter, glass doors and a bright ceiling light"></div>
<div class="hero-shade"></div>

<div class="logo-box"><span class="dot"></span><span class="name">Harbourline Press Works</span></div>

<div class="top-contact">416 555 0148<span>|</span>info@hpwdirect.example</div>

<nav class="main-nav">
  <a class="active" href="#">HOME</a>
  <a href="#">WHO WE ARE</a>
  <a href="#">WHAT WE DO</a>
  <a href="#">EMAIL A FILE</a>
  <a href="#">CONTACT US</a>
</nav>

<svg class="hero-arrow" style="left:80px" viewBox="0 0 37 37"><circle cx="18.5" cy="18.5" r="18.5" fill="rgba(200,200,200,.75)"/><path d="M21 11l-7 7.5 7 7.5" stroke="#fff" stroke-width="2" fill="none"/></svg>
<svg class="hero-arrow" style="left:945px" viewBox="0 0 37 37"><circle cx="18.5" cy="18.5" r="18.5" fill="rgba(200,200,200,.75)"/><path d="M16 11l7 7.5-7 7.5" stroke="#fff" stroke-width="2" fill="none"/></svg>

<section class="content">
  <h1>Welcome to our site</h1>
  <p>We maintain absolute integrity in every aspect of our operation. By using our experience to understand our customers' expectations, we show an uncommon commitment to achieving a high-quality product under strict deadlines. It is the customers who set the standards we strive to achieve. We are professionals who bring unique and specialized skills you can depend on.</p>
  <p>Pellentesque tincidunt gravida porta. Nullam ut elementum sapien. Pellentesque velit purus, adipiscing et condimentum sed, blandit ut velit. Duis fringilla leo non sem sodales at laoreet elit suscipit. Aenean justo dui, fringilla sit amet sagittis sed, tristique sed metus. Pellentesque congue mi at diam scelerisque id pharetra ipsum tristique. Fusce libero erat, scelerisque at mollis commodo, malesuada eu orci. Cras pellentesque mauris sed sapien sollicitudin vulputate. Nulla pharetra posuere odio ac viverra magna sed quam tincidunt tristique.</p>
</section>

<ul class="services">
  <li><svg width="13" height="13" viewBox="0 0 13 13"><circle cx="6.5" cy="6.5" r="6.5" fill="#333"/><path d="M5 4l2.5 2.5L5 9" stroke="#fff" stroke-width="1.5" fill="none"/></svg>DIGITAL PRINTING</li>
  <li><svg width="13" height="13" viewBox="0 0 13 13"><circle cx="6.5" cy="6.5" r="6.5" fill="#666"/><path d="M5 4l2.5 2.5L5 9" stroke="#fff" stroke-width="1.5" fill="none"/></svg>COMMERCIAL PRINTING</li>
  <li><svg width="13" height="13" viewBox="0 0 13 13"><circle cx="6.5" cy="6.5" r="6.5" fill="#666"/><path d="M5 4l2.5 2.5L5 9" stroke="#fff" stroke-width="1.5" fill="none"/></svg>LEGAL SERVICES</li>
  <li><svg width="13" height="13" viewBox="0 0 13 13"><circle cx="6.5" cy="6.5" r="6.5" fill="#666"/><path d="M5 4l2.5 2.5L5 9" stroke="#fff" stroke-width="1.5" fill="none"/></svg>MAILING HOUSE</li>
  <li><svg width="13" height="13" viewBox="0 0 13 13"><circle cx="6.5" cy="6.5" r="6.5" fill="#666"/><path d="M5 4l2.5 2.5L5 9" stroke="#fff" stroke-width="1.5" fill="none"/></svg>COMPUTER SERVICES</li>
  <li><svg width="13" height="13" viewBox="0 0 13 13"><circle cx="6.5" cy="6.5" r="6.5" fill="#666"/><path d="M5 4l2.5 2.5L5 9" stroke="#fff" stroke-width="1.5" fill="none"/></svg>FREE PICKUP &amp; DELIVERY</li>
</ul>

<div class="divider"></div>
<h2 class="works-title">Our Works</h2>

<svg class="works-arrow" style="left:87px" width="12" height="18" viewBox="0 0 12 18"><path d="M9 2L3 9l6 7" stroke="#666" stroke-width="3" fill="none"/></svg>
<svg class="works-arrow" style="left:958px" width="12" height="18" viewBox="0 0 12 18"><path d="M3 2l6 7-6 7" stroke="#666" stroke-width="3" fill="none"/></svg>

<div class="work" style="left:114px"><div class="frame"><div class="shot" role="img" aria-label="Wide-format digital printer producing a colourful poster" style="background:linear-gradient(#d8dadc,#b9a3b8 55%,#d6427c)"></div></div><p>Digital Printing</p></div>
<div class="work" style="left:327px"><div class="frame"><div class="shot" role="img" aria-label="Open printed brochure showing a car" style="background:linear-gradient(135deg,#c9d2dc,#5b5f66 60%,#2c2e33)"></div></div><p>Commercial Printing</p></div>
<div class="work" style="left:539px"><div class="frame"><div class="shot" role="img" aria-label="Stack of bound legal documents" style="background:linear-gradient(135deg,#f4f5f7,#dfe3e8 50%,#cfc2a6)"></div></div><p>Legal Services</p></div>
<div class="work" style="left:753px"><div class="frame"><div class="shot" role="img" aria-label="Mail inserting machinery in a production room" style="background:linear-gradient(#7f9aa8,#a9bcc4 50%,#5c7480)"></div></div><p>Mailing House</p></div>

<footer class="footer">
  <nav><a href="#">Home</a><span>|</span><a href="#">Who we are</a><span>|</span><a href="#">What we do</a><span>|</span><a href="#">Email a File</a><span>|</span><a href="#">Contact us</a></nav>
  <div class="copy">Copyright &nbsp;©&nbsp; 2013 &nbsp;www.hpwdirect.example &nbsp;&nbsp; All rights reserved</div>
  <span class="social" style="left:930px"></span>
  <span class="social" style="left:961px"></span>
</footer>
</body>
</html>
```